Wills & Estates legal firm needing A4 presentation folder design

We need a more corporate but family orientated looking presentation folder incorporating existing logo. Needs to be clean lines but warm not clinical. Will contain all documents a family needs when someone dies. Not looking for traditional legal symbols of scales etc. Potential that the design can flow through to letterhead, document front covers, brochures, business cards etc for a complete corporate identity. We are only a firm of one fee earner and cater to a mum and dad market

Industry/Entity Type

Law Firm

Font styles to use
Other font styles liked:
• Univers LT std 57 cn

Colors
ec1f27
848484

Requirements
Must have
• Existing logo
• Area for contact details on back of folder
• Incorporating existing red an grey colours
Should not have
• legal symbols

```html
<!DOCTYPE html>
<html lang="en">
<head>
<meta charset="utf-8">
<title>Keystone Legal — Presentation Folder</title>
<link rel="stylesheet" href="https://fonts.googleapis.com/css2?family=Libre+Caslon+Text&family=Questrial&display=swap">
<style>
  :root {
    --bg: #d9d9d9;
    --paper: #ffffff;
    --red: #c11230;
    --red-deep: #a40f28;
    --slate: #44545f;
    --ink: #4a4f54;
  }
  html, body {
    margin: 0;
    padding: 0;
    width: 1200px;
    height: 958px;
    overflow: hidden;
    background: var(--bg);
  }
  .spread {
    position: absolute;
    left: 34px;
    top: 79px;
    width: 1132px;
    height: 800px;
    background: var(--paper);
    box-shadow: 0 6px 24px rgba(0,0,0,0.18);
    overflow: hidden;
  }
  .feature-graphic {
    position: absolute;
    left: 300px;
    top: 0;
    width: 430px;
    height: 800px;
    background: linear-gradient(90deg, var(--red) 0%, var(--red-deep) 62%, var(--red) 100%);
  }
  .spine {
    position: absolute;
    left: 566px;
    top: 0;
    width: 1px;
    height: 800px;
    background: rgba(0,0,0,0.08);
  }
  .wordmark {
    position: absolute;
    margin: 0;
    font-family: "Libre Caslon Text", serif;
    font-weight: 400;
    color: var(--red);
    white-space: nowrap;
    letter-spacing: 0.2px;
  }
  .wordmark--front {
    left: 752px;
    top: 72px;
    font-size: 34px;
  }
  .wordmark--back {
    left: 50px;
    top: 654px;
    font-size: 19px;
  }
  .contact {
    position: absolute;
    left: 50px;
    top: 690px;
    font-family: "Questrial", sans-serif;
    font-size: 10.5px;
    line-height: 14px;
    color: var(--ink);
  }
  .contact-list {
    list-style: none;
    margin: 0 0 6px;
    padding: 0;
  }
  .contact-item {
    display: flex;
    align-items: center;
    gap: 6px;
  }
  .contact-icon {
    width: 9px;
    height: 9px;
    background: var(--red);
    border-radius: 1px;
    flex: none;
  }
  .contact-address {
    margin: 0;
    font-style: normal;
  }
</style>
</head>
<body>
  <main class="spread" aria-label="Presentation folder, back and front covers">
    <div class="feature-graphic" role="img" aria-label="Red and slate feature graphic crossing the folder spine"></div>
    <div class="spine" aria-hidden="true"></div>

    <p class="wordmark wordmark--front">Keystone Legal</p>

    <p class="wordmark wordmark--back">Keystone Legal</p>
    <div class="contact">
      <ul class="contact-list">
        <li class="contact-item"><span class="contact-icon"></span>03 5550 1842</li>
        <li class="contact-item"><span class="contact-icon"></span>admin@keystonelegal.com.au</li>
        <li class="contact-item"><span class="contact-icon"></span>www.keystonelegal.com.au</li>
      </ul>
      <address class="contact-address">14 Linden Street<br>NORTHWOOD VIC 3999</address>
    </div>
  </main>
</body>
</html>
```